Law Firm Header Revision

Task: Redesign my law firm Word document header (modern, succinct, logo-first, easy address updates)

I need you to revise and modernize my Microsoft Word document header for Law Office of Corbin Alvey, PLLC. The result should look professional and clean on letters (including Letters of Protection), with the logo as the main focus and the text kept succinct.

Goals:
1. Create a modern, minimal header that feels premium and uncluttered.
Make the logo the most visually dominant element.
Reduce the visual weight of the contact/address block so it doesn’t distract from the document.
Make the address easy to change later (I’m moving offices soon) while keeping the same header design.

2. Content to include (keep all info accurate):
Law Office of Corbin Alvey, PLLC
615 Marlowe St. Ste #300-214, Houston, TX 77002
Office: 832.555.0143
Direct: 713.555.0186
Fax: 832.555.0127
Calveylegal.example

3. Layout requirements:
Provide 3 header style options:
Logo left + contact info right
Centered logo + single concise contact line below
Logo left + firm name prominent + minimal contact line
The primary line near the logo should be minimal (preferably website + main office phone).
The address should be easy to update in one place without redesigning the header. Prefer either:
Move the full address to the footer, or
Put the address in a single dedicated line/block so I can edit it once and keep the layout unchanged.
4. Build constraints:
Must be achievable using standard Microsoft Word tools only (header/footer, tables, alignment, fonts, spacing). No advanced graphics software.
Provide exact header text, plus step-by-step Word instructions for each option:
Font recommendations + sizes
Alignment
Spacing
Table setup (if used)
How to keep it consistent across pages

5. Deliverable:
For each of the 3 options, provide:
The exact header content (with line breaks)
Formatting specs (fonts, sizes, spacing)
Word build steps so I can recreate it reliably and keep the logo as the focal point.

```html
<!DOCTYPE html>
<html lang="en">
<head>
<meta charset="utf-8">
<title>Corbin Alvey Law – Letterhead Options</title>
<link href="https://fonts.googleapis.com/css2?family=Poppins:wght@400;500;600&display=swap" rel="stylesheet">
<style>
  :root {
    --navy: #0c1725;
    --gold: #d39a48;
    --gold-deep: #bd9440;
    --paper: #ffffff;
    --backdrop: #eeeced;
    --ink-light: #ffffff;
  }
  * { box-sizing: border-box; margin: 0; padding: 0; }
  html, body { width: 960px; height: 1200px; overflow: hidden; }
  body {
    position: relative;
    background: var(--backdrop);
    font-family: "Poppins", sans-serif;
    color: var(--ink-light);
  }
  .sheet {
    position: absolute;
    width: 403.5px;
    height: 521.5px;
    background: var(--paper);
    overflow: hidden;
  }
  .sheet--centered { left: 61.8px; top: 70.7px; }
  .sheet--split { left: 494.7px; top: 70.7px; }
  .sheet--minimal { left: 285px; top: 619.4px; }

  .band { position: absolute; left: 0; width: 100%; background: var(--navy); }

  /* Wordmark */
  .wordmark { display: flex; align-items: center; gap: 5px; }
  .wordmark__square { width: 22px; height: 22px; background: var(--ink-light); }
  .wordmark__name {
    font-weight: 400; font-size: 13px; letter-spacing: 0.6px;
    color: var(--ink-light); white-space: nowrap;
  }

  /* Contact items */
  .contact { display: flex; align-items: center; gap: 5px; }
  .contact__icon {
    width: 16.5px; height: 16.5px; border-radius: 50%;
    background: var(--gold-deep);
    display: flex; align-items: center; justify-content: center;
  }
  .contact__icon svg { width: 7px; height: 7px; fill: var(--navy); }
  .contact__label { display: block; font-size: 6.3px; color: var(--gold-deep); line-height: 1.3; }
  .contact__value { display: block; font-size: 6.3px; font-weight: 600; color: var(--ink-light); line-height: 1.5; }

  .address-line {
    display: flex; align-items: center; justify-content: center; gap: 4px;
    font-size: 6.2px; font-weight: 600; white-space: nowrap;
  }
  .address-line svg { width: 5px; height: 6px; }

  /* Option 1 */
  .sheet--centered .header { top: 0; height: 46.7px; display: flex; align-items: center; justify-content: center; }
  .sheet--centered .address-band {
    position: absolute; top: 46.7px; left: 0; width: 100%; height: 15.6px;
    background: var(--gold); color: var(--navy);
  }
  .sheet--centered .address-band .address-line { height: 100%; }
  .sheet--centered .address-band svg { fill: var(--navy); }
  .sheet--centered .footer-tab { position: absolute; left: 0; top: 485.3px; width: 100%; height: 3.6px; }
  .sheet--centered .footer { top: 488.7px; height: 32.8px; }
  .sheet--centered .contact { position: absolute; top: 8px; }

  /* Option 2 */
  .sheet--split .header { top: 0; height: 61.8px; border-bottom: 2.2px solid var(--gold); }
  .sheet--split .header .wordmark { position: absolute; left: 18px; top: 19px; }
  .sheet--split .header .contact { position: absolute; top: 21px; }
  .sheet--split .footer-tab { position: absolute; left: 0; top: 481.4px; width: 100%; height: 19.6px; }
  .tab-line {
    position: absolute; top: 481.4px; left: 86px; width: 230px; height: 19.6px;
    display: flex; align-items: center; justify-content: center; gap: 26px;
    font-size: 6.2px; font-weight: 600; color: var(--ink-light);
  }
  .tab-line span { display: flex; align-items: center; gap: 6px; }
  .tab-line svg { width: 6px; height: 6px; fill: var(--ink-light); }
  .sheet--split .footer { top: 501px; height: 20.5px; display: flex; align-items: center; justify-content: center; }
  .sheet--split .footer svg { fill: var(--ink-light); }

  /* Option 3 */
  .sheet--minimal .header { top: 0; height: 67.9px; border-bottom: 2.2px solid var(--gold); }
  .sheet--minimal .header .wordmark { position: absolute; left: 0; width: 100%; top: 11px; justify-content: center; }
  .primary-line {
    position: absolute; left: 0; width: 100%; top: 49px;
    text-align: center; font-size: 10px; font-weight: 400; letter-spacing: 0.2px;
    word-spacing: 1px; white-space: nowrap;
  }
  .sheet--minimal .footer { top: 475.9px; height: 45.6px; text-align: center; }
  .footer__firm { font-size: 8.6px; margin-top: 5px; letter-spacing: 0.2px; }
  .footer__address, .footer__numbers { font-size: 6.3px; line-height: 1.7; }
  .footer__address { margin-top: 3px; }
</style>
</head>
<body>

<svg width="0" height="0" style="position:absolute" aria-hidden="true">
  <defs>
    <symbol id="icon-phone" viewBox="0 0 24 24"><path d="M6.6 10.8a15.1 15.1 0 0 0 6.6 6.6l2.2-2.2a1 1 0 0 1 1-.25 11.4 11.4 0 0 0 3.6.57 1 1 0 0 1 1 1V20a1 1 0 0 1-1 1A17 17 0 0 1 3 4a1 1 0 0 1 1-1h3.5a1 1 0 0 1 1 1c0 1.25.2 2.45.57 3.57a1 1 0 0 1-.25 1z"/></symbol>
    <symbol id="icon-globe" viewBox="0 0 24 24"><circle cx="12" cy="12" r="10"/></symbol>
    <symbol id="icon-fax" viewBox="0 0 24 24"><path d="M7 2h8l3 3v5h2a2 2 0 0 1 2 2v8a2 2 0 0 1-2 2H4a2 2 0 0 1-2-2v-8a2 2 0 0 1 2-2h3zm2 2v6h7V6h-3V4zM6 14v2h3v-2zm5 0v2h3v-2zm5 0v2h3v-2z"/></symbol>
    <symbol id="icon-pin" viewBox="0 0 20 24"><path d="M10 0a8 8 0 0 0-8 8c0 6 8 16 8 16s8-10 8-16a8 8 0 0 0-8-8zm0 11a3 3 0 1 1 0-6 3 3 0 0 1 0 6z"/></symbol>
  </defs>
</svg>

<!-- Option 1: centered wordmark -->
<section class="sheet sheet--centered" aria-label="Letterhead option one">
  <header class="band header">
    <div class="wordmark"><span class="wordmark__square"></span><span class="wordmark__name">CORBIN ALVEY LAW</span></div>
  </header>
  <div class="address-band">
    <p class="address-line"><svg viewBox="0 0 20 24"><use href="#icon-pin"/></svg>Law Office of Corbin Alvey, PLLC ,615 Marlowe St. Ste #300-214, Houston, TX 77002</p>
  </div>
  <svg class="footer-tab" viewBox="0 0 403.5 3.6" preserveAspectRatio="none"><polygon points="92,0 310,0 311.5,3.6 90.5,3.6" fill="var(--gold-deep)"/></svg>
  <footer class="band footer">
    <div class="contact" style="left:32.5px">
      <span class="contact__icon"><svg viewBox="0 0 24 24"><use href="#icon-phone"/></svg></span>
      <span><span class="contact__label">Office</span><span class="contact__value">832.555.0143</span></span>
    </div>
    <div class="contact" style="left:116px">
      <span class="contact__icon"><svg viewBox="0 0 24 24"><use href="#icon-globe"/></svg></span>
      <span><span class="contact__label">Website</span><span class="contact__value">www.Calveylegal.example</span></span>
    </div>
    <div class="contact" style="left:227.5px">
      <span class="contact__icon"><svg viewBox="0 0 24 24"><use href="#icon-phone"/></svg></span>
      <span><span class="contact__label">Direct</span><span class="contact__value">713.555.0186</span></span>
    </div>
    <div class="contact" style="left:309.5px">
      <span class="contact__icon"><svg viewBox="0 0 24 24"><use href="#icon-fax"/></svg></span>
      <span><span class="contact__label">Fax</span><span class="contact__value">832.555.0127</span></span>
    </div>
  </footer>
</section>

<!-- Option 2: wordmark left, contact right -->
<section class="sheet sheet--split" aria-label="Letterhead option two">
  <header class="band header">
    <div class="wordmark"><span class="wordmark__square"></span><span class="wordmark__name">CORBIN ALVEY LAW</span></div>
    <div class="contact" style="left:220.5px">
      <span class="contact__icon"><svg viewBox="0 0 24 24"><use href="#icon-phone"/></svg></span>
      <span><span class="contact__label">Office</span><span class="contact__value">832.555.0143</span></span>
    </div>
    <div class="contact" style="left:294.5px">
      <span class="contact__icon"><svg viewBox="0 0 24 24"><use href="#icon-globe"/></svg></span>
      <span><span class="contact__label">Website</span><span class="contact__value">www.Calveylegal.example</span></span>
    </div>
  </header>
  <svg class="footer-tab" viewBox="0 0 403.5 19.6" preserveAspectRatio="none"><polygon points="92.4,0 310.5,0 316.1,19.6 86.3,19.6" fill="var(--gold-deep)"/></svg>
  <p class="tab-line">
    <span><svg viewBox="0 0 24 24"><use href="#icon-phone"/></svg>Direct: 713.555.0186</span>
    <span><svg viewBox="0 0 24 24"><use href="#icon-fax"/></svg>Fax: 832.555.0127</span>
  </p>
  <footer class="band footer">
    <p class="address-line"><svg viewBox="0 0 20 24"><use href="#icon-pin"/></svg>Law Office of Corbin Alvey, PLLC ,615 Marlowe St. Ste #300-214, Houston, TX 77002</p>
  </footer>
</section>

<!-- Option 3: wordmark with single primary line -->
<section class="sheet sheet--minimal" aria-label="Letterhead option three">
  <header class="band header">
    <div class="wordmark"><span class="wordmark__square"></span><span class="wordmark__name">CORBIN ALVEY LAW</span></div>
    <p class="primary-line">832.555.0143 &nbsp;|&nbsp; www.Calveylegal.example</p>
  </header>
  <footer class="band footer">
    <p class="footer__firm">Law Office of Corbin Alvey, PLLC</p>
    <p class="footer__address">615 Marlowe St. Ste #300-214, Houston, TX 77002</p>
    <p class="footer__numbers">Office: 832.555.0143 &nbsp;|&nbsp; Direct: 713.555.0186 &nbsp;|&nbsp; Fax: 832.555.0127</p>
  </footer>
</section>

</body>
</html>
```